Cobalt Haulage needs Bussiness cards!

Our new trucking company needs business cards!
We need the same design with two different names and emails, everything else it's the same.
I have included our original logo so we can use it for the design.
Note: the logo to be used is the o e with the buffalo on the right side, next to the letters B and E.

Target Market(s)

Trucking, refrigerated transportation, freight

Industry/Entity Type

Business

Contact Information for Business Card

Card #1:
Marcos Varela
marcosvarela@cobalthaulage.net
1-833-617-4928
(575)738-2196
3817 W. Tinsley Ave.
Harlow, NM 88219
www.cobalthaulage.net

Card#2:
Marisol Trevino
marisol@cobalthaulage.net
1-833-617-4928
(575)738-2196
3817 W. Tinsley Ave.
Harlow, NM 88219
www.cobalthaulage.net

Font styles to use
Sans Serif

Colors
0655a3
ec1f27
ffffff

Requirements
Must have
• our logo
Nice to have
• roads on background,

```html
<!DOCTYPE html>
<html lang="en">
<head>
<meta charset="utf-8">
<title>Cobalt Haulage – Business Cards</title>
<link rel="stylesheet" href="https://fonts.googleapis.com/css2?family=Open+Sans:wght@400;600;800&display=swap">
<style>
  :root {
    --backdrop: #3b3532;
    --card-dark: #141414;
    --card-light: #ffffff;
    --brand-blue: #0655a3;
    --brand-red: #ec1f27;
    --text-light: #f2f2f2;
    --ghost: #efefef;
  }
  * { box-sizing: border-box; margin: 0; padding: 0; }
  html, body {
    width: 1200px; height: 900px; overflow: hidden;
    background: var(--backdrop);
    font-family: "Open Sans", Arial, sans-serif;
  }
  .canvas { position: relative; width: 1200px; height: 900px; }
  .card {
    position: absolute; top: 300px;
    width: 520px; height: 297px;
    border-radius: 3px;
    box-shadow: 0 12px 30px rgba(0,0,0,.45);
    overflow: hidden;
  }
  .card--front { left: 50px; background: var(--card-dark); color: var(--text-light); }
  .card--back { left: 630px; background: var(--card-light); }

  .wordmark {
    position: absolute; display: flex; align-items: center; gap: 10px;
    font-weight: 800; line-height: 1; letter-spacing: -0.5px; white-space: nowrap;
  }
  .wordmark__dot { width: 22px; height: 22px; border-radius: 50%; background: var(--brand-red); flex: none; }
  .card--front .wordmark { left: 48px; top: 72px; font-size: 34px; color: var(--text-light); }
  .card--back .wordmark { left: 150px; top: 126px; font-size: 34px; color: var(--brand-blue); }

  .rule { position: absolute; height: 2px; background: var(--brand-blue); }
  .rule--upper { left: 286px; right: 0; top: 128px; }
  .rule--lower { left: 0; width: 286px; top: 196px; }

  .holder { position: absolute; right: 34px; top: 146px; text-align: right; }
  .holder__name { color: var(--brand-red); font-size: 15px; font-weight: 600; margin-bottom: 10px; }
  .holder__address { font-size: 12.5px; line-height: 1.5; }

  .contacts { position: absolute; left: 40px; top: 210px; list-style: none; }
  .contacts li { display: flex; align-items: center; gap: 8px; font-size: 12.5px; line-height: 18px; }
  .contacts svg { width: 10px; height: 10px; fill: var(--brand-red); flex: none; }

  .ghost-mark {
    position: absolute; left: 30px; top: 20px; width: 240px; height: 240px;
    border-radius: 50%; background: var(--ghost);
  }
</style>
</head>
<body>
<main class="canvas">
  <section class="card card--front" aria-label="Business card front">
    <div class="wordmark"><span class="wordmark__dot"></span>Cobalt Haulage</div>
    <div class="rule rule--upper"></div>
    <div class="rule rule--lower"></div>
    <div class="holder">
      <p class="holder__name">Marcos Varela</p>
      <p class="holder__address">3817 W. Tinsley Ave.<br>Harlow, NM 88219</p>
    </div>
    <ul class="contacts">
      <li><svg viewBox="0 0 10 10"><rect x="2.5" y="0" width="5" height="10" rx="1"/></svg>1-833-617-4928</li>
      <li><svg viewBox="0 0 10 10"><path d="M1 2 Q1 0 3 0 L3 3 L2 4 Q3 6.5 6 8 L7 7 L10 7 Q10 10 8 10 Q1 9 1 2Z"/></svg>(575)738-2196</li>
      <li><svg viewBox="0 0 10 10"><path d="M0 2h10v6H0z M0 2l5 3.5L10 2"/></svg>marcosvarela@cobalthaulage.net</li>
      <li><svg viewBox="0 0 10 10"><circle cx="5" cy="5" r="5"/></svg>www.cobalthaulage.net</li>
    </ul>
  </section>

  <section class="card card--back" aria-label="Business card back">
    <div class="ghost-mark" role="img" aria-label="Faint brand emblem"></div>
    <div class="wordmark"><span class="wordmark__dot"></span>Cobalt Haulage</div>
  </section>
</main>
</body>
</html>
```